Motor Vault Website - Part of the Brantley Group

A complimentary website is required for the launch of a 'Motor Vault' - a new service launched by industry renowned BRANTLEY. Motor Vault is an industry-first brand that designs and builds unique subterranean car parks for private residential homes in London and the influential counties within the UK. Please see here the direction of a new BRANTLEY Website - we would like Motor Vault to be complimentary and sit alongside BRANTLEY harmoniously - https://www.brantleyhomes.example/brantley-nu-staging Brantley have some images, but whilst more professional images are in production - we have also attached pixmora photos- named clearly as pixmora. **Attached files include JPEG, .eps of logo and Brantley library images and Pixmora Library Images - two versions of logo dependent on background colour. - Website needs to be sleek, chic and masculine.- Colour Palette - Grey/ Black/ White - Same visiual journey as Brantley website- Required areas within the sit include - About Us / Our Work / Contact Page

Target Market(s)

Luxury
Men

Number of Pages Required

2 page

Font styles to use
Sans Serif

Colors
e8e8e8
757575
1b1b1b
000000
9d9d9d
cbcbcb
f5f5f5

Requirements
Must have
• Complimentary of this site - https://www.brantleyhomes.example/brantley-nu-staging
Should not have
• Colour

```html
<!DOCTYPE html>
<html lang="en">
<head>
<meta charset="utf-8">
<title>Motor Vault — Part of the Brantley Group</title>
<link rel="stylesheet" href="https://fonts.googleapis.com/css2?family=Roboto:wght@300;400;500;700&family=Montserrat:wght@300;400;500&display=swap">
<style>
  :root {
    --black: #000000;
    --ink: #1b1b1b;
    --grey-dark: #757575;
    --grey-mid: #9d9d9d;
    --grey-light: #cbcbcb;
    --mist: #e8e8e8;
    --paper: #ffffff;
  }
  * { box-sizing: border-box; margin: 0; padding: 0; }
  html, body { width: 1200px; height: 1000px; overflow: hidden; background: var(--paper); }
  body { font-family: 'Roboto', Arial, sans-serif; color: var(--black); position: relative; }

  .hero {
    position: absolute; left: 0; top: 0; width: 1200px; height: 705px;
    background:
      radial-gradient(ellipse 260px 380px at 660px 600px, rgba(200,200,200,0.35), transparent 70%),
      linear-gradient(90deg, #0c0c0c 0%, #2a2a2a 20%, #4a4a4a 40%, #3a3a3a 55%, #2e2e2e 75%, #141414 100%);
  }
  .site-header {
    position: absolute; left: 0; top: 0; width: 1200px; height: 66px;
    background: rgba(30,30,30,0.85);
  }
  .main-nav {
    position: absolute; right: 38px; top: 24px;
    display: flex; gap: 15px;
    font-size: 12.5px; letter-spacing: 0.2px; color: var(--mist);
  }
  .main-nav a { color: inherit; text-decoration: none; }
  .main-nav a.current { color: var(--paper); font-weight: 700; }

  .brand {
    position: absolute; left: 308px; top: 305px; width: 590px;
    font-family: 'Montserrat', Arial, sans-serif; color: var(--mist);
    display: flex; align-items: center; gap: 16px;
  }
  .brand-square { width: 58px; height: 58px; background: var(--mist); flex: none; }
  .brand-text { flex: 1; }
  .brand-name { font-size: 70px; font-weight: 500; line-height: 70px; letter-spacing: 1px; white-space: nowrap; }
  .brand-tagline { font-size: 14px; font-weight: 400; text-align: right; margin-top: 2px; letter-spacing: 0.3px; }

  .services {
    position: absolute; top: 758px; left: 0; width: 1200px;
    text-align: center; font-size: 31px; font-weight: 500; color: var(--black);
  }
  .services .arrow { font-size: 18px; vertical-align: 4px; margin: 0 12px 0 8px; }
  .intro {
    position: absolute; top: 826px; left: 0; width: 1200px;
    text-align: center; font-size: 15.5px; line-height: 24px; font-weight: 300; color: var(--ink);
  }
  .division {
    position: absolute; top: 932px; width: 474px;
    text-align: center; font-size: 15.5px; font-weight: 500;
  }
  .division-structural { left: 97px; }
  .division-interiors { left: 624px; }
  .division-image {
    margin-top: 22px; height: 40px;
    background: linear-gradient(180deg, #3a3a3a, #9d9d9d 60%, #cbcbcb);
  }
</style>
</head>
<body>
  <section class="hero" role="img" aria-label="Black and white photograph of a long concrete colonnade corridor"></section>

  <header class="site-header">
    <nav class="main-nav">
      <a class="current" href="#">HOME</a>
      <a href="#">STRUCTURAL</a>
      <a href="#">INTERIORS</a>
      <a href="#">ABOUT</a>
      <a href="#">PORTFOLIO</a>
      <a href="#">NEWS</a>
      <a href="#">CONTACT</a>
    </nav>
  </header>

  <div class="brand">
    <div class="brand-square"></div>
    <div class="brand-text">
      <div class="brand-name">MOTOR VAULT</div>
      <div class="brand-tagline">PART OF THE BRANTLEY GROUP</div>
    </div>
  </div>

  <h2 class="services">SHELL &amp; CORE<span class="arrow">&#9658;</span>BASEMENTS<span class="arrow">&#9658;</span>INTERIORS</h2>
  <p class="intro">Specialising turnkey solutions for Basements, Shell &amp;<br>Core and Interior Fit-Out in London and the Home Counties.</p>

  <section class="division division-structural">
    <h3 style="font-size:inherit;font-weight:inherit">STRUCTURAL DIVISION</h3>
    <div class="division-image" role="img" aria-label="Black and white photograph of exposed structural beams"></div>
  </section>
  <section class="division division-interiors">
    <h3 style="font-size:inherit;font-weight:inherit">INTERIORS DIVISION</h3>
    <div class="division-image" role="img" aria-label="Black and white photograph of an interior ceiling with lighting"></div>
  </section>
</body>
</html>
```